Breezeway Climate Business Card Design

Design new, 2 sides, business cards for a residential and light commercial heating, air conditioning contractor.

Target Market(s)

Homeowners, small businesses

Industry/Entity Type

Business

Contact Information for Business Card

Dominic Vasquerelli
Phone - 555-214-6837
Email
Address - PO box 618
Millbrook NJ 07999
Website - www.BreezewayClimateLLC.example

Requirements
Must have
• logo, company colors, standard size with no die cut, so I can use printhaven

```html
<!DOCTYPE html>
<html lang="en">
<head>
<meta charset="utf-8">
<title>Breezeway Climate Business Card</title>
<link href="https://fonts.googleapis.com/css2?family=PT+Sans:wght@400;700&display=swap" rel="stylesheet">
<style>
  :root {
    --backdrop: #141414;
    --card-light: #f3f3f3;
    --card-red: #9c2231;
    --brand-red: #8f1d2b;
    --brand-orange: #f39a1e;
    --brand-cream: #f8e4b0;
    --ink: #2a2a2a;
  }
  * { margin: 0; padding: 0; box-sizing: border-box; }
  html, body {
    width: 1200px;
    height: 900px;
    overflow: hidden;
    background: var(--backdrop);
    font-family: "PT Sans", Arial, sans-serif;
  }
  .canvas {
    position: relative;
    width: 1200px;
    height: 900px;
  }
  .card {
    position: absolute;
    top: 184px;
    height: 490px;
    border-radius: 14px;
  }
  .card-front {
    left: 299px;
    width: 301px;
    background: var(--card-light);
  }
  .card-back {
    left: 645px;
    width: 305px;
    background: var(--card-red);
  }
  .wordmark {
    position: absolute;
    left: 0;
    right: 0;
    display: flex;
    flex-direction: column;
    align-items: center;
    justify-content: center;
    text-align: center;
    font-weight: 700;
    text-transform: uppercase;
    letter-spacing: 1px;
    line-height: 1.05;
  }
  .card-front .wordmark {
    top: 71px;
    height: 142px;
    font-size: 40px;
    color: var(--brand-red);
  }
  .card-back .wordmark {
    top: 163px;
    height: 165px;
    font-size: 46px;
    color: var(--brand-cream);
  }
  .contact {
    position: absolute;
    top: 257px;
    left: 0;
    right: 0;
    text-align: center;
    color: var(--ink);
    font-size: 14px;
    line-height: 17.5px;
  }
  .person-name {
    font-size: 17px;
    font-weight: 700;
    line-height: 20px;
  }
  .first-name { color: var(--brand-red); }
  .last-name { color: var(--brand-orange); }
  .address { margin-top: 12px; }
  .reach { margin-top: 14px; }
</style>
</head>
<body>
  <main class="canvas">
    <section class="card card-front" aria-label="Card front">
      <div class="wordmark"><span>Breezeway</span><span>Climate</span></div>
      <div class="contact">
        <p class="person-name"><span class="first-name">Dominic</span> <span class="last-name">Vasquerelli</span></p>
        <p class="job-title">Managing Director</p>
        <p class="address">PO box 618<br>Millbrook NJ 07999</p>
        <p class="reach">555-214-6837<br>info@breezewayclimate.example<br>www.BreezewayClimateLLC.example</p>
      </div>
    </section>
    <section class="card card-back" aria-label="Card back">
      <div class="wordmark"><span>Breezeway</span><span>Climate</span></div>
    </section>
  </main>
</body>
</html>
```